I need a design with just the number 24. must be in blue color (royal blue) should be large enough for people see must be in the center of page. Place a nice border around the page.

Requirements
Must have
• Number 24 in Royal blue color

```html
<!DOCTYPE html>
<html lang="en">
<head>
<meta charset="utf-8">
<title>Number 24 Poster</title>
<link rel="stylesheet" href="https://fonts.googleapis.com/css2?family=Graduate&display=swap">
<style>
  :root {
    --royal-blue: #1c00a3;
    --paper: #ffffff;
  }
  html, body {
    margin: 0;
    padding: 0;
    overflow: hidden;
    background: var(--paper);
  }
  .poster {
    position: relative;
    width: 960px;
    height: 1200px;
    background: var(--paper);
    overflow: hidden;
  }
  .poster-border,
  .poster-number {
    position: absolute;
    inset: 0;
    width: 960px;
    height: 1200px;
  }
  .border-outer,
  .border-inner {
    fill: none;
    stroke: var(--royal-blue);
    stroke-width: 16;
  }
  .number-text {
    font-family: "Graduate", "Arial Black", sans-serif;
    font-size: 690px;
  }
  .number-outline {
    fill: var(--royal-blue);
    stroke: var(--royal-blue);
    stroke-width: 34;
    stroke-linejoin: miter;
  }
  .number-gap {
    fill: var(--royal-blue);
    stroke: var(--paper);
    stroke-width: 22;
    stroke-linejoin: miter;
  }
  .number-fill {
    fill: var(--royal-blue);
  }
</style>
</head>
<body>
  <main class="poster">
    <svg class="poster-border" viewBox="0 0 1263 1634" preserveAspectRatio="none" aria-hidden="true">
      <path class="border-outer"
        d="M192,31 H1070 A148,148 0 0 0 1218,178 V1470 A148,148 0 0 0 1070,1603 H192 A148,148 0 0 0 44,1470 V178 A148,148 0 0 0 192,31 Z"/>
      <rect class="border-inner" x="87" y="90" width="1089" height="1453"/>
    </svg>

    <svg class="poster-number" viewBox="0 0 960 1200">
      <text class="number-text number-outline" x="104" y="836" textLength="752" lengthAdjust="spacingAndGlyphs" aria-hidden="true">24</text>
      <text class="number-text number-gap" x="104" y="836" textLength="752" lengthAdjust="spacingAndGlyphs" aria-hidden="true">24</text>
      <text class="number-text number-fill" x="104" y="836" textLength="752" lengthAdjust="spacingAndGlyphs">24</text>
    </svg>
  </main>
</body>
</html>
```